依頼詳細
■商品の特徴
・使用する原材料は「小麦粉・塩・水」のみ。厳選した国産小麦粉をたっぷりの水で捏ね、みずみずしい透明感とツヤのある麺に仕上げました。
・麺の太さは、細すぎず、適度な噛みごたえ、食べ応えが楽しめます。
・油を使っていないシンプルな原材料で安心感も併せて訴求。

■デザインの方向性
・和紙(雲竜またはカルミナ)の風合いを生かす
・和モダン、シンプル、品がある、
・素朴で田舎っぽいがお洒落なイメージも想起させる。
・夏、涼しい、冷たい、水、流れ、波紋など、涼感を想起させるイメージ。
・商品名が筆文字の場合は、達筆すぎない、崩れすぎていない、読みやすいこと。

■留意点
・ジジ臭いのはNG(蕎麦やうどんは、とかくジジ臭くなりがちです)

■ 利用用途
・決定したデザインはそうめんの他、冷麦などシリーズ展開します。
記載項目
■パッケージ仕様
・商品名:青峰の細打ち冷や糸(仮名)
・フィルム寸法:W230×H275(オモテ面 W100×H275の範囲をデザイン)
・フィルム材質:レーヨン紙(雲竜またはカルミナ)
・色数:5色まで(シズルは無し)
希望イメージ
シンプル 複雑
単色 カラフル
暗い 明るい
日常 高級
遊び心 厳粛
未来的 伝統的
女性的 男性的
希望する色
青系、水色系、グレー系、紫系
納品ファイル
• 高解像度JPG (.jpg)
• イラストレーター形式 (.ai)
• フォトショップ形式 (.psd)
補足説明
合成用の画像を用意しましたので、可能であればこの画像に合成してご提案いただけますでしょか?よろしくお願い致します。
■ 選んだ理由

和風、モダンさのバランスが求めていたものに近い気がしました。売り場のイメージにもマッチしていると感じました。色を変えてのシリーズ展開もしやすそうでした。白を生かした涼感も感じました。

■ 提案者全員のお礼・コメント

この度は素敵なデザインのご提案ありがとうございます。こちらのデザインを元に修正もお願いするかと思います。その際はよろしくお願いいたします。
まずは、修正の方向性を私の方で探って見たいので、イラレのデータをいただけますでしょうか?よろしくお願いいたします。

```html
<!DOCTYPE html>
<html lang="ja">
<head>
<meta charset="utf-8">
<title>青峰の細打ち冷や糸</title>
<link rel="stylesheet" href="https://fonts.googleapis.com/css2?family=Shippori+Mincho:wght@500;700&family=Noto+Serif+JP:wght@400;600&display=swap">
<style>
  :root {
    --paper: #ffffff;
    --wave: #9fd5e8;
    --wave-soft: #d6eef6;
    --ink: #2b2b2b;
    --emblem: #e6e8ea;
    --emblem-light: #f4f5f6;
  }
  html, body {
    margin: 0;
    padding: 0;
    width: 1200px;
    height: 3232px;
    overflow: hidden;
    background: var(--paper);
  }
  .label {
    position: relative;
    width: 1200px;
    height: 3232px;
    background: var(--paper);
    font-family: "Noto Serif JP", serif;
    color: var(--ink);
  }
  .wave-band {
    position: absolute;
    left: 0;
    width: 1200px;
  }
  .wave-band--top {
    top: 30px;
    height: 110px;
    background: linear-gradient(0deg, var(--wave-soft), var(--wave));
  }
  .wave-band--bottom {
    top: 2810px;
    height: 390px;
    background: linear-gradient(180deg, var(--wave-soft), var(--wave));
  }

  .emblem {
    position: absolute;
    left: 290px;
    top: 200px;
    width: 520px;
    height: 600px;
    border-radius: 60px;
    background: radial-gradient(circle at 50% 50%, var(--emblem-light), var(--emblem));
  }

  .title {
    position: absolute;
    margin: 0;
    writing-mode: vertical-rl;
    font-family: "Shippori Mincho", serif;
    color: var(--ink);
    line-height: 1;
  }
  .title__lead {
    left: 650px;
    top: 870px;
    font-size: 84px;
    font-weight: 500;
    letter-spacing: 8px;
  }
  .title__main {
    left: 440px;
    top: 1010px;
    font-size: 170px;
    font-weight: 700;
    letter-spacing: 30px;
  }

  .story {
    position: absolute;
    left: 370px;
    top: 2000px;
    width: 770px;
    height: 760px;
    border-top: 10px solid var(--ink);
    border-left: 2px solid var(--ink);
    border-right: 2px solid var(--ink);
    box-sizing: border-box;
    padding: 40px 34px;
  }
  .story__text {
    writing-mode: vertical-rl;
    height: 100%;
    margin: 0 0 0 auto;
    font-size: 34px;
    line-height: 1.95;
    letter-spacing: 1px;
    color: var(--ink);
  }
</style>
</head>
<body>
  <main class="label">
    <div class="wave-band wave-band--top" role="img" aria-label="水色の青海波文様の帯"></div>

    <div class="emblem" role="img" aria-label="流れる麺と稲穂を描いた紋章イラスト"></div>

    <h1 class="title title__lead">青峰の細打ち</h1>
    <p class="title title__main">冷や糸</p>

    <section class="story">
      <p class="story__text">使用する原材料は「小麦粉・塩・水」のみ。厳選した国産小麦粉をたっぷりの水で捏ね、みずみずしい透明感とツヤのある麺に仕上げました。麺の太さは、細すぎず、適度な噛みごたえ、食べ応えが楽しめます。油を使っていないシンプルな原材料で安心してお召し上がりいただけます。</p>
    </section>

    <div class="wave-band wave-band--bottom" role="img" aria-label="水色の青海波文様の帯"></div>
  </main>
</body>
</html>
```